Brisk Comet- Energy shot - ....Amazing Energy for Amazing people

To design a creative /unique logo and picture for Brisk Comet Energy/ energy shot product similar to Zippo Day energy shot...Berry flavor

I want the design to cover the entire bottle. in addition to Logo (Brisk Comet Energy )

So Brisk Comet Energy will be a competitor of Zippo Day energy and I want a creative,fantastic, attractive design to catch customers eyes, the product will be in similar size 2oz bottle (see attached image). This template is based on a common 2oz bottle size that measures exactly 114mm circumference x 83mm-85mm height (including cap ).
Please include At the top cap a Logo for: Brisk Comet...

Target Market(s)

Young, busy professionals, athletics

Industry/Entity Type

Product

Logo Text

Quorva Energy...Amazing Energy &Taste !

Requirements
Must have
• Creative exciting design...Quorva Energy...Fan
Nice to have
• Be a genius....Be creative...Be Amazing !

```html
<!DOCTYPE html>
<html lang="en">
<head>
<meta charset="utf-8">
<title>Brisk Comet Energy – Berry Label</title>
<link rel="stylesheet" href="https://fonts.googleapis.com/css2?family=Roboto+Condensed:ital,wght@0,700;1,700&family=Roboto:wght@400&display=swap">
<style>
  :root {
    --label-yellow: #fff200;
    --brand-red: #e8202a;
    --ink: #111111;
    --white: #ffffff;
    --badge-green: #9cc83e;
    --splash-orange: #f08a1c;
    --splash-red: #c4301c;
    --splash-dark: #7a1a12;
  }
  * { margin: 0; padding: 0; box-sizing: border-box; }
  html, body { width: 895px; height: 1200px; overflow: hidden; background: var(--label-yellow); }
  .label {
    position: relative;
    width: 895px;
    height: 1200px;
    background: var(--label-yellow);
    overflow: hidden;
    font-family: "Roboto Condensed", sans-serif;
  }
  .cap-brand {
    position: absolute;
    left: 300px;
    top: 135px;
    display: flex;
    align-items: center;
    gap: 18px;
  }
  .cap-brand__name {
    font-weight: 700;
    font-size: 38px;
    line-height: 1;
    color: var(--brand-red);
    text-transform: uppercase;
    letter-spacing: 1px;
  }
  .cap-brand__dot {
    width: 58px;
    height: 58px;
    border-radius: 50%;
    background: var(--badge-green);
  }
  .cap-divider {
    position: absolute;
    left: 0;
    top: 301px;
    width: 100%;
    height: 5px;
    background: var(--white);
  }
  .brand-title {
    position: absolute;
    left: 285px;
    top: 380px;
    color: var(--brand-red);
    font-weight: 700;
    text-transform: uppercase;
    line-height: 1;
  }
  .brand-title__line { display: block; font-size: 58px; letter-spacing: 2px; }
  .brand-title__line--first { margin-left: 84px; }
  .brand-title__line--second { font-size: 76px; margin-top: 6px; letter-spacing: 4px; }
  .benefits {
    position: absolute;
    left: 384px;
    top: 520px;
    list-style: none;
  }
  .benefits__item {
    display: flex;
    align-items: center;
    gap: 14px;
    height: 51px;
    font-style: italic;
    font-weight: 700;
    font-size: 38px;
    color: var(--ink);
  }
  .benefits__tick { width: 34px; height: 32px; flex: none; }
  .action-art {
    position: absolute;
    left: 0;
    top: 730px;
    width: 895px;
    height: 470px;
    background:
      radial-gradient(ellipse at 62% 35%, var(--splash-dark) 0 10%, transparent 30%),
      linear-gradient(165deg, var(--label-yellow) 0%, var(--splash-orange) 30%, var(--splash-red) 65%, var(--splash-dark) 100%);
  }
  .claims {
    position: absolute;
    left: 210px;
    top: 790px;
    color: var(--white);
    font-style: italic;
    font-weight: 700;
    font-size: 24px;
    letter-spacing: 1px;
    text-transform: uppercase;
    line-height: 38px;
  }
  .product-facts {
    position: absolute;
    left: 107px;
    right: 89px;
    top: 1144px;
    display: flex;
    justify-content: space-between;
    font-family: "Roboto", sans-serif;
    font-size: 25px;
    color: var(--white);
    text-transform: uppercase;
  }
</style>
</head>
<body>
<main class="label">
  <div class="cap-brand">
    <span class="cap-brand__name">Brisk Comet Energy</span>
    <span class="cap-brand__dot"></span>
  </div>

  <div class="cap-divider"></div>

  <h1 class="brand-title">
    <span class="brand-title__line brand-title__line--first">Brisk Comet</span>
    <span class="brand-title__line brand-title__line--second">Energy</span>
  </h1>

  <ul class="benefits">
    <li class="benefits__item"><svg class="benefits__tick" viewBox="0 0 34 32"><path d="M3 17 L12 27 L31 4" fill="none" stroke="#111" stroke-width="6" stroke-linecap="round" stroke-linejoin="round"/></svg>Hour of energy now</li>
    <li class="benefits__item"><svg class="benefits__tick" viewBox="0 0 34 32"><path d="M3 17 L12 27 L31 4" fill="none" stroke="#111" stroke-width="6" stroke-linecap="round" stroke-linejoin="round"/></svg>No crash later</li>
    <li class="benefits__item"><svg class="benefits__tick" viewBox="0 0 34 32"><path d="M3 17 L12 27 L31 4" fill="none" stroke="#111" stroke-width="6" stroke-linecap="round" stroke-linejoin="round"/></svg>Sugar free</li>
    <li class="benefits__item"><svg class="benefits__tick" viewBox="0 0 34 32"><path d="M3 17 L12 27 L31 4" fill="none" stroke="#111" stroke-width="6" stroke-linecap="round" stroke-linejoin="round"/></svg>0 net carbs</li>
  </ul>

  <div class="action-art" role="img" aria-label="Sprinting athlete silhouette over orange and red paint splashes"></div>

  <p class="claims">Feel it in minutes<br>Lasts for hour</p>

  <div class="product-facts">
    <span>Berry flavor</span>
    <span>2 fl oz (60ml)</span>
    <span>Vitamin supplement</span>
  </div>
</main>
</body>
</html>
```